Postcard Design for Marketing to Builders

I am an architect that gets most of my work from contractor's. I design residential and commercial projects based in California. My main focus is California's Central Coast. I want the feel of the postcard to reflect a strong professional, efficient and creative partner for contractors (Builders). I have provide some photos of projects I have done recently to use on the postcard if needed. I have also included my logo which I would like on the front.

Industry/Entity Type

Architect

Font styles to use
Serif

```html
<!DOCTYPE html>
<html lang="en">
<head>
<meta charset="utf-8">
<title>Daniel R Hale Architect Postcard</title>
<link href="https://fonts.googleapis.com/css2?family=Arimo:wght@400;700&family=Tinos:wght@400;700&display=swap" rel="stylesheet">
<style>
  :root {
    --page: #e6e6e4;
    --navy: #2c4699;
    --navy-deep: #233a84;
    --orange: #f07c1d;
    --white: #ffffff;
    --ink: #2c4699;
    --sky-top: #5f9fd8;
    --sky-low: #d9e8f5;
  }
  * { margin: 0; padding: 0; box-sizing: border-box; }
  html, body { width: 819px; height: 1200px; overflow: hidden; }
  body { background: var(--page); position: relative; font-family: "Arimo", Arial, sans-serif; }

  .card {
    position: absolute; left: 88px; width: 642px; height: 494px;
    background: var(--white); overflow: hidden;
    box-shadow: 0 3px 10px rgba(0,0,0,0.25);
  }
  .card--front { top: 64px; }
  .card--back { top: 626px; }
  .card-art { position: absolute; inset: 0; width: 642px; height: 494px; }

  .brand {
    position: absolute; display: flex; align-items: center; gap: 8px;
    font-family: "Tinos", "Times New Roman", serif; font-weight: 700;
    color: var(--navy); font-size: 20px; white-space: nowrap;
  }
  .brand-mark { width: 22px; height: 22px; background: var(--orange); }
  .card--front .brand { left: 28px; top: 52px; }
  .card--back .brand { left: 470px; top: 400px; }

  .intro { position: absolute; left: 365px; top: 26px; width: 262px; text-align: center; color: var(--white); }
  .intro-name { font-family: "Tinos", "Times New Roman", serif; font-weight: 400; font-size: 30px; letter-spacing: 0.5px; }
  .intro-text { margin-top: 10px; font-size: 11.5px; line-height: 1.5; }

  .email {
    position: absolute; color: var(--white); font-weight: 700; font-size: 17px; white-space: nowrap;
  }
  .card--front .email { right: 20px; top: 400px; }
  .card--back .email { left: 24px; top: 400px; }

  .call { position: absolute; left: 0; top: 14px; width: 300px; text-align: center; color: var(--ink); font-family: "Tinos", "Times New Roman", serif; font-weight: 700; }
  .call-label { font-size: 20px; }
  .call-phone { font-size: 26px; letter-spacing: 0.5px; }

  .address { position: absolute; left: 40px; top: 440px; width: 260px; text-align: center; color: var(--white); font-size: 13px; line-height: 1.35; }

  .stamp { position: absolute; left: 507px; top: 35px; width: 95px; height: 96px; border: 1px solid #555; }
</style>
</head>
<body>

<section class="card card--front" aria-label="Postcard front">
  <svg class="card-art" viewBox="0 0 642 494" aria-hidden="false">
    <defs>
      <linearGradient id="lodgeTone" x1="0" y1="0" x2="0" y2="1">
        <stop offset="0" stop-color="#8fbbe6"/>
        <stop offset="0.3" stop-color="#c9ddf0"/>
        <stop offset="0.42" stop-color="#b04a3a"/>
        <stop offset="0.6" stop-color="#a7683c"/>
        <stop offset="1" stop-color="#6b5646"/>
      </linearGradient>
      <linearGradient id="officeTone" x1="0" y1="0" x2="0" y2="1">
        <stop offset="0" stop-color="#7eb0e4"/>
        <stop offset="0.45" stop-color="#d4e4f2"/>
        <stop offset="0.7" stop-color="#6f8a4e"/>
        <stop offset="1" stop-color="#4d6a3a"/>
      </linearGradient>
    </defs>
    <rect width="642" height="494" fill="url(#lodgeTone)" role="img" aria-label="Photo of a timber lodge with red roof and stone chimney"/>
    <rect x="0" y="0" width="260" height="130" fill="#e7f0f9" opacity="0.55"/>
    <path d="M266 0 Q427.5 247 279 494 L642 494 L642 0 Z" fill="var(--navy)"/>
    <rect x="355" y="197" width="287" height="170" fill="url(#officeTone)" role="img" aria-label="Photo of a single-storey office building with lawn"/>
    <rect x="355" y="367" width="287" height="5" fill="var(--white)"/>
    <rect x="300" y="395" width="342" height="35" fill="var(--orange)"/>
    <rect x="330" y="440" width="312" height="54" fill="var(--navy-deep)" opacity="0.6"/>
    <path d="M262 0 Q423.5 247 275 494" fill="none" stroke="var(--white)" stroke-width="6"/>
    <path d="M270 0 Q431.5 247 283 494" fill="none" stroke="var(--orange)" stroke-width="6"/>
  </svg>

  <div class="brand"><span class="brand-mark"></span>Daniel R Hale</div>

  <div class="intro">
    <h1 class="intro-name">DANIEL HALE</h1>
    <p class="intro-text">A licensed architect for over 25 years.<br>He has designed everything from a<br>single family residence to a 3 story office<br>building. He has worked with hundreds<br>of clients and has helped them see their<br>vision become a reality.</p>
  </div>

  <p class="email">Dan@DanielHaleStudio.com</p>
</section>

<section class="card card--back" aria-label="Postcard back">
  <svg class="card-art" viewBox="0 0 642 494">
    <defs>
      <linearGradient id="skyTone" x1="0" y1="0" x2="0" y2="1">
        <stop offset="0" stop-color="var(--sky-top)"/>
        <stop offset="1" stop-color="var(--sky-low)"/>
      </linearGradient>
      <linearGradient id="buildingTone" x1="0" y1="0" x2="0" y2="1">
        <stop offset="0" stop-color="#cfe0f0"/>
        <stop offset="0.25" stop-color="#c9b394"/>
        <stop offset="0.65" stop-color="#8a8068"/>
        <stop offset="1" stop-color="#4f6a3c"/>
      </linearGradient>
    </defs>
    <path d="M0 0 L279 0 Q375 230 300 494 L0 494 Z" fill="url(#skyTone)"/>
    <path d="M0 95 L320 95 Q340 250 318 395 L0 395 Z" fill="url(#buildingTone)" role="img" aria-label="Photo of a multi-storey office building with landscaped entry"/>
    <path d="M0 395 L345 395 L330 412 L345 430 L0 430 Z" fill="var(--orange)"/>
    <path d="M0 430 L318 430 Q312 465 300 494 L0 494 Z" fill="var(--navy)"/>
    <path d="M279 0 Q375 230 300 494" fill="none" stroke="var(--orange)" stroke-width="7"/>
  </svg>

  <div class="call">
    <p class="call-label">Call Us Today!</p>
    <p class="call-phone">(209) 555-0148</p>
  </div>

  <p class="email">Dan@DanielHaleStudio.com</p>
  <p class="address">PO Box 2200, Morro Bay,<br>CA 93442.</p>

  <div class="stamp" aria-label="Stamp area"></div>
  <div class="brand"><span class="brand-mark"></span>Daniel R Hale</div>
</section>

</body>
</html>
```